Design a Small Graphic for a client brochure and Website

We need a a fairly simple diagram/graphic to replace the existing graphic in our brochures and website. We are a Private Wealth Advice firm, dealing with high-end clients. We would like to be able to copyright the final design. We need this design to be stylish and have a long shelf-life.
The original design is quite old and was not updated to reflect our company growth or changes in our website design and brochure designs.
Updates

Target Market(s)

Private Wealth clients
High end
Age 45 plus

Industry/Entity Type

Finance

Font styles to use
Sans Serif
Other font styles liked:
• Stag Sans

Requirements
Must have
• Corporate colours only - plus white
• Pantone 288c (Blue)
• Pantone Cool grey 10c
• Pantone 666c (purple - only limited use for highlighting etc)
• Corporate fonts only
• Stag Sans light, book and thin
• Must provide AI editable files
• Must be able to scale to size and remove/replace any text
• Must be in keeping with our brochures and website which can be viewed at www.lorvane-advisory.com.au
Nice to have
• We want something more vibrant than the image we are using. Something which is in keeping with our image but that is really eye catching.

```html
<!DOCTYPE html>
<html lang="en">
<head>
<meta charset="utf-8">
<title>Relationship Management Diagram</title>
<link rel="stylesheet" href="https://fonts.googleapis.com/css2?family=Source+Sans+3:wght@300;400&display=swap">
<style>
  :root {
    --brand-blue: #002d72;
    --cool-grey: #63666a;
    --accent-purple: #a392b4;
    --white: #ffffff;
  }
  html, body {
    margin: 0;
    padding: 0;
    width: 1200px;
    height: 1000px;
    overflow: hidden;
    background: var(--white);
  }
  .canvas {
    width: 1200px;
    height: 1000px;
    display: block;
  }
  .service-wheel__disc { fill: var(--brand-blue); }
  .service-wheel__divider { fill: var(--white); }
  .service-wheel__accent-arc {
    fill: none;
    stroke: var(--accent-purple);
    stroke-width: 3;
  }
  .hub__outer-ring { fill: var(--cool-grey); }
  .hub__inner-ring { fill: var(--accent-purple); }
  .hub__core { fill: var(--white); }
  .service-label {
    font-family: "Source Sans 3", sans-serif;
    font-weight: 300;
    font-size: 23px;
    letter-spacing: 1.5px;
    fill: var(--white);
  }
  .hub__label {
    font-family: "Source Sans 3", sans-serif;
    font-weight: 400;
    font-size: 24px;
    fill: var(--cool-grey);
  }
</style>
</head>
<body>
<svg class="canvas" viewBox="0 0 1200 1000" role="img" aria-label="Relationship Management at the centre of Purpose, Investment Consulting, Wealth Planning and Your Legacy">
  <defs>
    <path id="arc-top-outer" d="M 432 500 A 168 168 0 0 1 768 500"/>
    <path id="arc-top-mid" d="M 452 500 A 148 148 0 0 1 748 500"/>
    <path id="arc-top-inner" d="M 461 500 A 139 139 0 0 1 739 500"/>
    <path id="arc-bottom-inner" d="M 436 500 A 164 164 0 0 0 764 500"/>
    <path id="arc-bottom-outer" d="M 409 500 A 191 191 0 0 0 791 500"/>
  </defs>

  <g class="service-wheel">
    <circle class="service-wheel__disc" cx="600" cy="500" r="216"/>
    <rect class="service-wheel__divider" x="592" y="280" width="16" height="440"/>
    <rect class="service-wheel__divider" x="380" y="492" width="440" height="16"/>

    <path class="service-wheel__accent-arc" d="M 560 337 A 168 168 0 0 1 640 337"/>
    <path class="service-wheel__accent-arc" d="M 763 460 A 168 168 0 0 1 763 540"/>
    <path class="service-wheel__accent-arc" d="M 640 663 A 168 168 0 0 1 560 663"/>
    <path class="service-wheel__accent-arc" d="M 437 540 A 168 168 0 0 1 437 460"/>

    <text class="service-label"><textPath href="#arc-top-mid" startOffset="25%" text-anchor="middle">Purpose</textPath></text>
    <text class="service-label"><textPath href="#arc-top-outer" startOffset="75%" text-anchor="middle">Investment</textPath></text>
    <text class="service-label"><textPath href="#arc-top-inner" startOffset="75%" text-anchor="middle">Consulting</textPath></text>
    <text class="service-label"><textPath href="#arc-bottom-inner" startOffset="25%" text-anchor="middle">Your</textPath></text>
    <text class="service-label"><textPath href="#arc-bottom-outer" startOffset="25%" text-anchor="middle">Legacy</textPath></text>
    <text class="service-label"><textPath href="#arc-bottom-inner" startOffset="75%" text-anchor="middle">Wealth</textPath></text>
    <text class="service-label"><textPath href="#arc-bottom-outer" startOffset="75%" text-anchor="middle">Planning</textPath></text>
  </g>

  <g class="hub">
    <circle class="hub__outer-ring" cx="600" cy="500" r="116"/>
    <circle class="hub__inner-ring" cx="600" cy="500" r="106"/>
    <circle class="hub__core" cx="600" cy="500" r="93"/>
    <text class="hub__label" x="600" text-anchor="middle">
      <tspan x="600" y="492">Relationship</tspan>
      <tspan x="600" y="525">Management</tspan>
    </text>
  </g>
</svg>
</body>
</html>
```